Northfield Builders Guild Business card

We are looking for a new business card design with photo included.
Our business is a nonprofit construction contractor membership organization. We offer business education, assist with business setup and licensing, provide safety training, and provide a member directory.
URL: www.brickwayguildnetwork.org
Color code:
CMYK: 0 cyan, 42 magenta, 100 yellow, 0 black for Print.
Hexidecimal: #FF9900
RGB: R 255; G 153; B 0

```html
<!DOCTYPE html>
<html lang="en">
<head>
<meta charset="utf-8">
<title>Northfield Builders Guild Business Card</title>
<link href="https://fonts.googleapis.com/css2?family=Open+Sans:wght@400;800&display=swap" rel="stylesheet">
<style>
  :root {
    --page: #ffffff;
    --card-light: #ffffff;
    --card-shade: #e6e6e8;
    --ink: #111111;
    --brand-orange: #ea9220;
    --bar-black: #000000;
  }
  * { margin: 0; padding: 0; box-sizing: border-box; }
  html, body { width: 1200px; height: 1000px; overflow: hidden; background: var(--page); }
  body { position: relative; font-family: "Open Sans", Arial, sans-serif; color: var(--ink); }

  .business-card {
    position: absolute;
    width: 676px;
    height: 386px;
    background: linear-gradient(110deg, var(--card-light) 0%, #f7f7f8 45%, var(--card-shade) 100%);
    overflow: hidden;
  }
  .card-front { left: 275px; top: 52px; }
  .card-back  { left: 273px; top: 521px; }

  .accent-bar-black {
    position: absolute; left: 0; top: 0;
    width: 347px; height: 23px;
    background: var(--bar-black);
  }
  .accent-bar-orange {
    position: absolute; right: 0; bottom: 0;
    width: 328px; height: 23px;
    background: var(--brand-orange);
  }

  .guild-name {
    position: absolute; left: 0; right: 0; top: 122px;
    text-align: center;
    font-weight: 800;
    font-size: 34px;
    letter-spacing: -0.3px;
    color: var(--ink);
    text-transform: uppercase;
  }

  .contact-list { position: absolute; list-style: none; }
  .contact-list li {
    display: flex; align-items: center; gap: 9px;
    height: 31px; font-size: 17px; white-space: nowrap;
  }
  .contact-left  { left: 38px; top: 262px; }
  .contact-right { right: 40px; top: 257px; text-align: right; }
  .contact-right li { justify-content: flex-end; height: 34px; }
  .contact-icon { width: 24px; height: 24px; flex: none; }
</style>
</head>
<body>

<section class="business-card card-front" aria-label="Business card">
  <div class="accent-bar-black"></div>
  <h1 class="guild-name">Northfield Builders Guild</h1>
  <ul class="contact-list contact-left">
    <li>
      <svg class="contact-icon" viewBox="0 0 24 24" aria-hidden="true"><rect x="1" y="4" width="22" height="16" fill="#ea9220"/><path d="M1 4 L12 13 L23 4 M1 20 L9 11 M23 20 L15 11" stroke="#fff" stroke-width="1.5" fill="none"/></svg>
      <span>support@northfieldguild.org</span>
    </li>
    <li>
      <svg class="contact-icon" viewBox="0 0 24 24" aria-hidden="true"><g fill="none" stroke="#ea9220" stroke-width="2"><circle cx="12" cy="12" r="10"/><ellipse cx="12" cy="12" rx="4.5" ry="10"/><path d="M2 12 H22 M4 7 H20 M4 17 H20"/></g></svg>
      <span>www.brickwayguildnetwork.org</span>
    </li>
  </ul>
  <ul class="contact-list contact-right">
    <li>
      <span>(555) 214-7730</span>
      <svg class="contact-icon" viewBox="0 0 24 24" aria-hidden="true"><path d="M2 9 Q12 1 22 9 L19 11 L16 8 L8 8 L5 11 Z" fill="#ea9220"/><path d="M6 11 L18 11 L20 21 L4 21 Z" fill="#ea9220"/><circle cx="12" cy="15.5" r="2.5" fill="#fff"/></svg>
    </li>
    <li>
      <span>555.308.1146</span>
      <svg class="contact-icon" viewBox="0 0 24 24" aria-hidden="true"><rect x="6" y="3" width="12" height="6" fill="#ea9220"/><rect x="2" y="9" width="20" height="9" rx="1" fill="#ea9220"/><rect x="6" y="15" width="12" height="7" fill="#fff" stroke="#ea9220" stroke-width="2"/></svg>
    </li>
  </ul>
  <div class="accent-bar-orange"></div>
</section>

<section class="business-card card-back" aria-label="Business card">
  <div class="accent-bar-black"></div>
  <h1 class="guild-name">Northfield Builders Guild</h1>
  <ul class="contact-list contact-left">
    <li>
      <svg class="contact-icon" viewBox="0 0 24 24" aria-hidden="true"><rect x="1" y="4" width="22" height="16" fill="#ea9220"/><path d="M1 4 L12 13 L23 4 M1 20 L9 11 M23 20 L15 11" stroke="#fff" stroke-width="1.5" fill="none"/></svg>
      <span>support@northfieldguild.org</span>
    </li>
    <li>
      <svg class="contact-icon" viewBox="0 0 24 24" aria-hidden="true"><g fill="none" stroke="#ea9220" stroke-width="2"><circle cx="12" cy="12" r="10"/><ellipse cx="12" cy="12" rx="4.5" ry="10"/><path d="M2 12 H22 M4 7 H20 M4 17 H20"/></g></svg>
      <span>www.brickwayguildnetwork.org</span>
    </li>
  </ul>
  <ul class="contact-list contact-right">
    <li>
      <span>(555) 214-7730</span>
      <svg class="contact-icon" viewBox="0 0 24 24" aria-hidden="true"><path d="M2 9 Q12 1 22 9 L19 11 L16 8 L8 8 L5 11 Z" fill="#ea9220"/><path d="M6 11 L18 11 L20 21 L4 21 Z" fill="#ea9220"/><circle cx="12" cy="15.5" r="2.5" fill="#fff"/></svg>
    </li>
    <li>
      <span>555.308.1146</span>
      <svg class="contact-icon" viewBox="0 0 24 24" aria-hidden="true"><rect x="6" y="3" width="12" height="6" fill="#ea9220"/><rect x="2" y="9" width="20" height="9" rx="1" fill="#ea9220"/><rect x="6" y="15" width="12" height="7" fill="#fff" stroke="#ea9220" stroke-width="2"/></svg>
    </li>
  </ul>
  <div class="accent-bar-orange"></div>
</section>

</body>
</html>
```